established boer goat stud and dorper sheep stud need an updated look

I need a design to promote the boer goat stud and dorper sheep stud, so its clear and simple

Details for business card design Tarwelle Boers and Dorper Sheep Stud. I would like silhouette animal head or full body of a boer goat (not a dairy breed goat) and Dorper sheep. Contact: Maree Cosgrove +61 412836507 Donna Petrakis +61 438571946 Kerrinvale North Victoria Australia Email: tarwelle5184@farmpost.net

Industry/Entity Type

Agriculture

Contact Information for Business Card

Tarwelle Boers and Dorper Sheep Stud Maree Cosgrove +61 412836507 Donna Petrakis +61 438571946 tarwelle5184@farmpost.net Kerrinvale Victoria Australia

Colors
EE7325
F08F49
F5BC92
FAE3D3
FDF4ED

Requirements
Must have
• My Boer Goats and Dorper Sheep images see my photos

```html
<!DOCTYPE html>
<html lang="en">
<head>
<meta charset="utf-8">
<title>Tarwelle Boers and Dorper Stud – Business Card</title>
<link href="https://fonts.googleapis.com/css2?family=Anton&family=Lato:wght@400;700;900&display=swap" rel="stylesheet">
<style>
  :root {
    --page: #a9a9a9;
    --card-dark: #171412;
    --orange: #ee7325;
    --white: #ffffff;
    --grass: #5d6b3a;
    --soil: #6b5a45;
    --goat: #7a3a22;
    --fleece: #e8e0d2;
  }
  * { margin: 0; padding: 0; box-sizing: border-box; }
  html, body { width: 1200px; height: 900px; overflow: hidden; }
  body {
    background: var(--page);
    position: relative;
    font-family: "Lato", sans-serif;
  }
  .card {
    position: absolute;
    left: 250px;
    width: 700px;
    height: 400px;
    overflow: hidden;
    box-shadow: 0 10px 24px rgba(0,0,0,0.35);
  }
  .card--front { top: 40px; }
  .card--back {
    top: 470px;
    background: var(--card-dark);
    border-radius: 28px;
  }
  .studname {
    position: absolute;
    font-family: "Anton", sans-serif;
    font-weight: 400;
    font-size: 36px;
    line-height: 1.2;
    color: var(--white);
    text-transform: uppercase;
    letter-spacing: 0.5px;
    white-space: nowrap;
    text-shadow: 0 2px 6px rgba(0,0,0,0.5);
  }
  /* front */
  .front-photo {
    position: absolute; inset: 0;
    background:
      radial-gradient(ellipse at 72% 40%, var(--fleece) 0 18%, transparent 32%),
      radial-gradient(ellipse at 30% 78%, var(--goat) 0 22%, transparent 45%),
      linear-gradient(160deg, #2a2b22 0%, var(--grass) 45%, var(--soil) 100%);
  }
  .card--front .studname { left: 36px; top: 34px; }
  /* back */
  .card--back .studname { left: 34px; top: 96px; }
  .photo-circle {
    position: absolute;
    border-radius: 50%;
  }
  .photo-circle--sheep {
    left: 530px; top: -20px;
    width: 230px; height: 230px;
    background: radial-gradient(circle at 45% 55%, var(--fleece) 0 30%, #a5a37a 55%, var(--grass) 100%);
  }
  .photo-circle--goat {
    left: -30px; top: 215px;
    width: 300px; height: 300px;
    background: radial-gradient(circle at 55% 45%, #f1ede6 0 22%, #8a6a4c 50%, var(--soil) 100%);
  }
  .arcs { position: absolute; inset: 0; }
  .contacts {
    position: absolute;
    left: 318px; top: 168px;
    color: var(--white);
  }
  .contact__name {
    color: var(--orange);
    font-weight: 900;
    font-size: 24px;
    line-height: 1.1;
  }
  .contact__phone {
    font-size: 19px;
    letter-spacing: 1px;
    margin-bottom: 8px;
  }
  .contact__email {
    font-size: 18px;
    margin-top: 14px;
  }
  .contact__place {
    display: flex; align-items: center; gap: 8px;
    color: var(--orange);
    font-size: 19px;
    margin-top: 4px;
  }
</style>
</head>
<body>

  <section class="card card--front">
    <div class="front-photo" role="img" aria-label="Photo of a red Boer goat herd grazing beside Dorper sheep on green pasture"></div>
    <h1 class="studname">Tarwelle Boers and Dorper Stud</h1>
  </section>

  <section class="card card--back">
    <div class="photo-circle photo-circle--sheep" role="img" aria-label="Photo of a Dorper sheep lying on grass"></div>
    <div class="photo-circle photo-circle--goat" role="img" aria-label="Photo of a white Boer goat with a brown head standing in a paddock"></div>
    <svg class="arcs" width="700" height="400" viewBox="0 0 700 400" aria-hidden="true">
      <path d="M 519 110 A 128 128 0 0 0 756 159" fill="none" stroke="var(--orange)" stroke-width="5"/>
      <path d="M 525 51 A 128 128 0 0 1 572 -10" fill="none" stroke="var(--orange)" stroke-width="5"/>
      <path d="M -21 283 A 163 163 0 0 1 273 309" fill="none" stroke="var(--orange)" stroke-width="5"/>
      <path d="M 281 351 A 163 163 0 0 1 260 448" fill="none" stroke="var(--orange)" stroke-width="5"/>
    </svg>

    <h1 class="studname">Tarwelle Boers and Dorper Stud</h1>

    <div class="contacts">
      <p class="contact__name">Maree Cosgrove</p>
      <p class="contact__phone">+61 412836507</p>
      <p class="contact__name">Donna Petrakis</p>
      <p class="contact__phone">+61 438571946</p>
      <p class="contact__email">tarwelle5184@farmpost.net</p>
      <p class="contact__place">
        <svg width="16" height="20" viewBox="0 0 16 20" aria-hidden="true">
          <path d="M8 0 C3.6 0 0 3.4 0 7.6 C0 13 8 20 8 20 C8 20 16 13 16 7.6 C16 3.4 12.4 0 8 0 Z M8 10.5 A3 3 0 1 1 8 4.5 A3 3 0 1 1 8 10.5 Z" fill="var(--orange)"/>
        </svg>
        Kerrinvale Victoria Australia
      </p>
    </div>
  </section>

</body>
</html>
```